Website redesign for a Cloud Advisory business

We are looking to revisit our existing brand and website, with a view to updating both. Looking for concepts and designs for how the website might look, flow and feel. Current website is: www.brellomint.com.au

Scope and Deliverables: Concept design for the home page and one internal page.

We do not expect you to design all the pages and all the elements of the website at this stage.

This job is not for the full website design, but just for concepts that we can start with when we go into the full website design.

We would love to see a design feature based on our name, logo, or industry, which can run through banners and other collateral (twitter banner, ads on Google, corporate documents etc).

We want the brand to properly depict what we bring/deliver to businesses when consulting to them and this should extend to the colour scheme, logo, font (perhaps updated) and copy (which will be supplied).

Our brand should suitably communicate our ability, knowledge and extensive experience within the Cloud space.

It should express and evoke credibility, knowledge and understanding of the Cloud space, independence, gravitas, reliability, efficiency, trust, expertise, approachability, service delivery but be uncomplicated, practical and use plain speaking language.

Colours that reinforce this might include: Blues, blacks, silver, white, grey and our existing orange.

Website designs that we like or have referenced include:

Varnolift: http://varnolift.com.au/ - This has good information but looks a little amateur in it’s cartoon like design and colour scheme. Also, this seems to be aimed at clients more interested in price than design and what we are going for is a little more high end.

Pendramoor: https://www.pendramoor.com.au/ - This site has merit in its’ setup but little call to action on the home page, especially before the scroll line. I like the set up of the Case Studies page however I’d look to make it more prominent by having it set up 3 across rather than the 4 they have. Something such as this: https://www.qandelby.com/case-studies

Tolvane: http://www.tolvane.com.au/#home4 - This page is a good one as far as selling services and information on the company. I quite like it.

MirefoldIT: http://www.mirefoldit.com.au/ - While I don’t think is particularly creative, it does practically depict the services we offer in a fairly clear way and might be a bit of a basic (albeit dull) template to follow.

JDP: https://store.jdp.com/us/Product-Family/JDP-Advisory-Services/JDP-Cloud-Advisory-Service/p/JDP-Services-Cloud-Advisory - This offers substantial information but is probably a little confusing although the roll-over drop down menus have merit.

ZEV: http://www.zev.net.au/en/services/ - While this in not quite what we are looking for, the colour scheme gives it more gravitas and quality.

As another reference, this website and the way they present their case studies is also something we like, although I’d like them shown 3 up, side by side…. https://www.qandelby.com/case-studies.

We have added a page layout and page purpose document.

Target Market(s)

Corporates, small - medium business, direct referrals, via search results

Industry/Entity Type

Business

Number of Pages Required

1 page

Font styles to use
Sans Serif

Colors
85abd2
0455a3
000000
f37122
5c5c5c

Requirements
Must have
• Website must be mobile device compatible.
• Concept design for the home page.
Nice to have
• We would love to see a design feature based on our name, logo, or industry, which can run through banners and other collateral (twitter banner, ads on Google, corporate documents etc).

```html
<!DOCTYPE html>
<html lang="en">
<head>
<meta charset="utf-8">
<title>Brellomint – Impartial Cloud Solutions</title>
<link href="https://fonts.googleapis.com/css2?family=Questrial&display=swap" rel="stylesheet">
<style>
:root{
  --orange:#f37122;
  --orange-dark:#d95a12;
  --ink:#2b2b2b;
  --ink-deep:#1d1d1d;
  --text:#3a3a3a;
  --grey:#5c5c5c;
  --pale:#efefef;
  --white:#ffffff;
  --peach:#fde3cf;
}
*{box-sizing:border-box;margin:0;padding:0}
html,body{width:1200px;height:2703px;overflow:hidden}
body{position:relative;font-family:"Questrial",sans-serif;color:var(--text);background:var(--white)}
.abs{position:absolute}
a{color:inherit;text-decoration:none}

/* header */
.topline{left:0;top:0;width:1200px;height:7px;background:#555}
.header{left:0;top:7px;width:1200px;height:154px;background:linear-gradient(#fafafa,#ececec)}
.brand{left:50px;top:58px;display:flex;align-items:center;gap:14px}
.brand-mark{width:40px;height:40px;background:var(--orange)}
.brand-name{font-size:40px;letter-spacing:2px;color:var(--ink-deep)}
.search{left:835px;top:69px;width:182px;height:36px;border:1px solid #bbb;background:var(--white);font-size:14px;color:#999;padding:9px 12px;letter-spacing:1px}
.search svg{position:absolute;right:8px;top:8px}
.social{top:72px;width:30px;height:30px;border-radius:50%;background:#1f5fa8}

/* nav */
.nav{left:0;top:161px;width:1200px;height:41px;background:var(--ink)}
.nav a{position:absolute;top:0;height:41px;line-height:41px;font-size:14px;color:var(--white);text-transform:uppercase;letter-spacing:.5px}
.nav a.active{background:var(--orange);padding:0 11px}

/* hero */
.hero{left:0;top:202px;width:1200px;height:472px;overflow:hidden}
.hero-photo{position:absolute;inset:0;background:radial-gradient(circle at 330px 200px,#6a6a6a,#2a2a2a 70%)}
.hero-panel{position:absolute;left:0;top:0}
.hero-title{position:absolute;left:745px;top:102px;width:404px;height:48px;background:#3a2a1c;transform:skewX(-18deg)}
.hero-title span,.hero-sub span{display:block;transform:skewX(18deg);text-align:center}
.hero-title span{font-size:38px;color:var(--white);letter-spacing:3px;line-height:48px}
.hero-sub{position:absolute;left:818px;top:156px;width:273px;height:45px;background:var(--peach);transform:skewX(-18deg)}
.hero-sub span{font-size:38px;color:var(--orange);letter-spacing:3px;line-height:45px}
.hero-copy{position:absolute;left:745px;top:216px;width:420px;text-align:center;font-size:23px;line-height:29px;color:var(--white);letter-spacing:1px}
.btn-outline,.btn-dark{position:absolute;top:335px;height:41px;line-height:41px;text-align:center;font-size:17px;color:var(--white);letter-spacing:1px}
.btn-outline{left:775px;width:179px;border:1px solid var(--white)}
.btn-dark{left:969px;width:177px;background:#111}

/* solutions */
.solutions{left:0;top:674px;width:1200px;height:817px;background:var(--pale)}
.section-title{position:absolute;left:0;width:1200px;text-align:center;font-size:23px;letter-spacing:1.5px;color:var(--ink-deep);text-transform:uppercase}
.section-title em{font-style:normal;color:var(--orange)}
.intro{position:absolute;left:173px;top:120px;width:854px;text-align:center;font-size:19px;line-height:29px;letter-spacing:.6px;color:#444}
.card{position:absolute;top:258px;width:307px;height:373px;background:var(--white);box-shadow:0 3px 6px rgba(0,0,0,.12)}
.card-head{height:58px;background:var(--ink);color:var(--white);font-size:18px;letter-spacing:1.5px;text-transform:uppercase;display:flex;align-items:center;justify-content:center;text-align:center;line-height:22px}
.card-img{position:absolute;left:56px;top:56px;width:197px;height:132px}
.card-text{position:absolute;left:36px;top:203px;width:235px;text-align:center;font-size:14px;line-height:19px;color:#333}
.card-btn{position:absolute;left:101px;top:313px;width:105px;height:26px;line-height:26px;background:var(--orange);color:var(--white);text-align:center;font-size:13px}
.view-all{position:absolute;left:486px;top:710px;width:222px;height:56px;line-height:52px;background:var(--orange);border-bottom:4px solid var(--orange-dark);color:var(--white);text-align:center;font-size:21px;letter-spacing:1.5px}

/* about + blog */
.about{left:0;top:1491px;width:1200px;height:515px;background:linear-gradient(90deg,#232323,#3d3d3d 55%,#2a2a2a)}
.col-title{position:absolute;font-size:23px;letter-spacing:1.5px;color:var(--white);text-transform:uppercase;padding-bottom:12px;border-bottom:1px solid #888}
.col-title em{font-style:normal;color:var(--orange)}
.about-text{position:absolute;left:81px;top:144px;width:434px;font-size:15px;line-height:21.5px;color:var(--white);letter-spacing:.3px}
.about-text p+p{margin-top:21px}
.post{position:absolute;left:629px;width:470px;height:90px}
.post-thumb{position:absolute;left:0;top:0;width:126px;height:87px;border:3px solid #ddd;background:linear-gradient(#e8e8e8,#9c9c9c)}
.post-title{position:absolute;left:137px;top:0;font-size:15px;color:var(--orange);text-transform:uppercase}
.post-text{position:absolute;left:137px;top:20px;width:333px;font-size:15px;line-height:20px;color:var(--white)}
.all-articles{position:absolute;left:629px;top:385px;font-size:15px;color:var(--white);text-decoration:underline;letter-spacing:1px;text-transform:uppercase}

/* testimonial */
.testimonial{left:0;top:2006px;width:1200px;height:370px;background:var(--white)}
.testimonial .rule{position:absolute;left:200px;top:94px;width:800px;height:1px;background:#ddd}
.client{position:absolute;left:108px;top:160px;display:flex;align-items:center;gap:12px}
.client-mark{width:26px;height:26px;border-radius:50%;background:#6b4c9a}
.client-name{font-size:18px;line-height:22px;color:#2f6db5;width:160px}
.quote-mark{position:absolute;left:354px;top:140px;font-size:70px;color:var(--orange);line-height:1}
.quote{position:absolute;left:376px;top:159px;width:712px;font-size:19px;line-height:25px;color:#555;text-align:justify;letter-spacing:.5px}
.quote-name{position:absolute;left:376px;top:259px;font-size:19px;color:var(--orange);letter-spacing:1px}

/* footer */
.footer{left:0;top:2376px;width:1200px;height:293px;background:var(--ink)}
.foot-title{position:absolute;top:38px;font-size:16px;color:var(--white);letter-spacing:1.5px;text-transform:uppercase;padding-bottom:10px;border-bottom:1px solid #555}
.foot-links{position:absolute;top:90px;list-style:none;font-size:13px;line-height:23.5px;color:var(--white);letter-spacing:.5px}
.foot-sep{position:absolute;left:457px;top:186px;width:212px;height:1px;background:#555}
.field{position:absolute;background:var(--white);border:1px solid #ccc;font-size:12px;color:#888;padding:5px 8px}
.send{position:absolute;left:799px;top:219px;width:160px;height:34px;line-height:34px;background:var(--orange);color:var(--white);font-size:13px;text-align:center;text-transform:uppercase}
.bottom{left:0;top:2669px;width:1200px;height:34px;background:var(--orange)}
.bottom p{position:absolute;left:99px;top:9px;font-size:13px;color:var(--white)}
.bottom i{position:absolute;top:6px;width:22px;height:22px;border-radius:50%;background:var(--white)}
</style>
</head>
<body>

<div class="abs topline"></div>
<header class="abs header">
  <div class="abs brand"><span class="brand-mark"></span><span class="brand-name">BRELLOMINT</span></div>
  <div class="abs search">Keyword Search
    <svg width="20" height="20" viewBox="0 0 20 20"><circle cx="8" cy="8" r="5.5" fill="none" stroke="#999" stroke-width="2"/><line x1="12" y1="12" x2="17" y2="17" stroke="#999" stroke-width="2"/></svg>
  </div>
  <span class="abs social" style="left:1037px"></span>
  <span class="abs social" style="left:1076px;background:#2a9be0"></span>
  <span class="abs social" style="left:1113px;background:#1578b8"></span>
</header>

<nav class="abs nav">
  <a class="active" style="left:58px">Home</a>
  <a style="left:159px">About us</a>
  <a style="left:276px">Industry Specialties</a>
  <a style="left:486px">Solutions</a>
  <a style="left:614px">The Company We Keep</a>
  <a style="left:837px">Case Studies</a>
  <a style="left:985px">FAQ</a>
  <a style="left:1061px">Contact</a>
</nav>

<section class="abs hero">
  <div class="hero-photo" role="img" aria-label="Photo of a businessman in a suit touching a glowing cloud surrounded by app icons"></div>
  <svg class="hero-panel" width="1200" height="472" viewBox="0 0 1200 472">
    <defs><linearGradient id="heroOrange" x1="0" y1="0" x2="1" y2="1"><stop offset="0" stop-color="#f58a2c"/><stop offset="1" stop-color="#f37122"/></linearGradient></defs>
    <polygon points="786,0 1200,0 1200,472 596,472" fill="url(#heroOrange)"/>
  </svg>
  <div class="hero-title"><span>IMPARTIAL CLOUD</span></div>
  <div class="hero-sub"><span>SOLUTIONS</span></div>
  <p class="hero-copy">We provide impartial advice<br>on cloudsolutions ensuring<br>it's always right for you.</p>
  <a class="btn-outline">SOLUTIONS</a>
  <a class="btn-dark">CONTACT US</a>
</section>

<section class="abs solutions">
  <h2 class="section-title" style="top:40px">Our <em>Solutions</em></h2>
  <p class="intro">Lorem ipsum dolor sit amet, consectetur adipiscing elit. Phasellus eget leo leo. Sed adipiscing mi orci, vel ultrices turpis mattis a. Quisque sed eros luctus, euismod ligula et, suscipit dolor. Sed et fermentum erat.</p>

  <article class="card" style="left:63px">
    <h3 class="card-head">System Selection</h3>
    <div class="card-img" role="img" aria-label="Photo of a hand touching a network of cloud connections" style="background:linear-gradient(135deg,#9fc3de,#2d4d6e)"></div>
    <p class="card-text">Find the right systems for you. Devise a cloud strategy. Inventory Management. Point of Sale. Job Management. Time &amp; Attendance. CRM.</p>
    <a class="card-btn">Read more</a>
  </article>

  <article class="card" style="left:446px">
    <h3 class="card-head">Accounting Systems<br>&amp; Conversions</h3>
    <div class="card-img" role="img" aria-label="Photo of a hand holding a handheld scanner" style="background:linear-gradient(135deg,#d6d6d6,#8a8a8a)"></div>
    <p class="card-text">Convert your Ledgerly, Tallybook, Sumwise, Plainsbook, Netcount, Gridsheet to Kelvo.</p>
    <a class="card-btn">Read more</a>
  </article>

  <article class="card" style="left:829px">
    <h3 class="card-head">Integration</h3>
    <div class="card-img" role="img" aria-label="Photo of an open hand beneath glowing blue data" style="background:linear-gradient(135deg,#1e3f63,#3fa7d6)"></div>
    <p class="card-text">Find the right systems for you. Devise a cloud strategy. Inventory Management. Point of Sale. Job Management. Time &amp; Attendance. CRM.</p>
    <a class="card-btn">Read more</a>
  </article>

  <a class="view-all">VIEW ALL</a>
</section>

<section class="abs about" role="img" aria-label="Dimmed photo of a busy open-plan office">
  <h2 class="col-title" style="left:81px;top:78px;width:465px">Welcome to <em>Brellomint</em></h2>
  <div class="about-text">
    <p>Lorem ipsum dolor sit amet, consectetur adipiscing elit. Phasellus eget leo leo. Sed adipiscing mi orci, vel ultrices turpis mattis a. Quisque sed eros luctus, euismod ligula et, suscipit dolor. Sed suscipit tortor eget leo hendrerit semper. Sed et fermentum erat.</p>
    <p>Curabitur tristique vestibulum bibendum. Quisque eget varius eros. Nunc id laoreet sem. Nullam vulputate fringilla mi sit amet imperdiet. Lorem ipsum dolor sit amet, consectetur adipiscing elit. Pellentesque habitant morbi tristique senectus et netus et malesuada fames ac turpis egestas.</p>
  </div>

  <h2 class="col-title" style="left:623px;top:78px;width:467px">Latest <em>Blog</em></h2>
  <div class="post" style="top:139px">
    <div class="post-thumb" role="img" aria-label="Photo of a presenter at a whiteboard chart"></div>
    <h3 class="post-title">Article title goes here</h3>
    <p class="post-text">Lorem ipsum dolor sit amet, consectetur adipiscing elit. Phasellus eget leo leo. Sed adipiscing mi orci, vel ultrices turpis matti.</p>
  </div>
  <div class="post" style="top:274px">
    <div class="post-thumb" role="img" aria-label="Photo of a presenter at a whiteboard chart"></div>
    <h3 class="post-title">Article title goes here</h3>
    <p class="post-text">Lorem ipsum dolor sit amet, consectetur adipiscing elit. Phasellus eget leo leo. Sed adipiscing mi orci, vel ultrices turpis matti.</p>
  </div>
  <a class="all-articles">View all articles</a>
</section>

<section class="abs testimonial">
  <h2 class="section-title" style="top:46px">What are <em>clients says</em></h2>
  <div class="rule"></div>
  <div class="client"><span class="client-mark"></span><span class="client-name">Larkfield Women's Health Care</span></div>
  <div class="quote-mark">&ldquo;</div>
  <p class="quote">Fearing inevitable change from Sumwise to Kelvo I was nicely surprised and made to feel comfortable with something that simply works very well indeed. Maren is a dependable and knowledgeable person in this minefield of accounting software. Highly recommended."</p>
  <p class="quote-name">- Daniel Ossery</p>
</section>

<footer class="abs footer">
  <h3 class="foot-title" style="left:101px;width:246px">Quicklinks</h3>
  <ul class="foot-links" style="left:107px"><li>Home</li><li>Link 2</li><li>Link 3</li><li>Link 4</li><li>Link 5</li></ul>
  <ul class="foot-links" style="left:246px"><li>Link 6</li><li>Link 7</li><li>Link 8</li></ul>

  <h3 class="foot-title" style="left:457px;width:212px">Useful Information</h3>
  <ul class="foot-links" style="left:464px"><li>Sitemap</li><li>F.A.Q</li><li>Privacy Policy</li><li>Terms &amp; Conditions</li></ul>
  <div class="foot-sep"></div>
  <ul class="foot-links" style="left:464px;top:198px"><li>Melbourne, Victoria</li><li>1300 472 918</li><li>info@brellomint.com</li></ul>

  <h3 class="foot-title" style="left:793px;width:290px">Quick Message</h3>
  <div class="field" style="left:797px;top:83px;width:137px;height:28px">Firstname</div>
  <div class="field" style="left:943px;top:83px;width:137px;height:28px">Email Address</div>
  <div class="field" style="left:797px;top:121px;width:283px;height:83px">Message</div>
  <a class="send">Send message</a>
</footer>

<div class="abs bottom">
  <p>Brellomint Copyright 2016 All rights reserved</p>
  <i style="left:970px"></i><i style="left:998px"></i><i style="left:1026px"></i><i style="left:1054px"></i>
</div>

</body>
</html>
```